San Francisco Leading Consulting firm - 47Nova Web Design Project

•Create a Web Design
•Uncoded webpage layout design
•2 Pages Design - Homepage + Interior Page

Task Description
Hello, we're looking for a re-design our current website www.47nova-example.com

we have a sample mockup design @

http://47nova.civicpane-example.org/

This shows the layout that we like and also a sample of 6 pictures that would change based on where you mouse over..

6 pictures HOME design needs to be included.

SMART
THOUGHTFUL
FLEXIBLE
CREATIVE SERVICES
TECHNICAL SERVICES
PARTNERS

sites we like:

http://www.brelmoradvisory-example.com/Home.cfm?id=Home
http://www.pixelquarry-example.com/index.html

Our company can be best described as: 100+ employees, cutting-edge, depandable, innovative, strong, smart.

Our Primary focus is: IT Consulting Services and Creative Design services

47Nova LLC is a consulting firm providing creative design, business and technology solutions to both private and public interests.

Established in 1996, 47Nova is a San Francisco based company providing specialists for a range of business needs including:

Creative Design Services
•Print
•Logo Design
•Website Design
•Illustration

and

Business and Technology solutions

•Application Software and Web Development
•Business Process Re-Design (BPR)
•Business/Systems Analysis and Requirement Documentation
•Mentoring and Training
•Network/Hardware Installation Services
•System Design and Architecture
•Vendor Management
•Teamvault Architecture and Implementation

our sample mockup site:

Reason: Due to holiday season, we're not available to work with designers and finilize our design.  

Thank you very much for submitting your design.

We appreciate your time and creativity.   Since, our office is currently closed for holidays, we will be reviewing it in details next week and will make our decision as soon as possible.

It would be great if you could submit any of your changes by Wed next week, so it would be part of our reviews. 

Please see updated wireframe under attachments:  we have some minor updates to our wireframe that we would like you to update your designs, if possible.  

We also encorouge you not to use our standard wireframe and come up with more unique designs.   Everything would be considered when we review your design.

 

Target Market(s)

Creative services and professional services clients, including government agencies

Industry/Entity Type

Business

Requirements
Must have
• Clean, professional look, easy navigation

```html
<!DOCTYPE html>
<html lang="en">
<head>
<meta charset="utf-8">
<title>47Nova — Company</title>
<link href="https://fonts.googleapis.com/css2?family=Roboto+Condensed:wght@300;400;700&family=Arimo:wght@400;700&display=swap" rel="stylesheet">
<style>
  :root {
    --blue: #2f86c6;
    --nav-active: #e8f3fb;
    --line: #d9e6f0;
    --text: #5a5a5a;
    --heading: #555;
    --green: #8a9c14;
    --green-dark: #6e7e0c;
    --white: #fff;
  }
  * { box-sizing: border-box; margin: 0; padding: 0; }
  html, body { width: 1200px; height: 730px; overflow: hidden; background: var(--white); }
  body { position: relative; font-family: "Arimo", Arial, sans-serif; color: var(--text); }

  .brand { position: absolute; left: 224px; top: 16px; display: flex; align-items: center; gap: 8px; }
  .brand-dot { width: 34px; height: 34px; border-radius: 50%; background: var(--blue); }
  .brand-name { font-family: "Roboto Condensed", sans-serif; font-size: 27px; color: #333; letter-spacing: 1px; }

  .main-nav { position: absolute; left: 440px; top: 0; width: 536px; height: 78px; display: flex;
    border-left: 1px solid var(--line); border-right: 1px solid var(--line); border-bottom: 1px solid var(--line); border-bottom-right-radius: 8px; }
  .nav-item { position: relative; height: 77px; display: flex; align-items: center; justify-content: center;
    font-family: "Roboto Condensed", sans-serif; font-size: 13px; letter-spacing: -0.3px; color: var(--blue);
    border-right: 1px solid var(--line); padding-bottom: 1px; }
  .nav-item:last-child { border-right: none; }
  .nav-item.is-active { background: var(--nav-active); }
  .nav-item.is-active::after { content: ""; position: absolute; bottom: -1px; left: 50%; margin-left: -7px;
    border-left: 7px solid transparent; border-right: 7px solid transparent; border-bottom: 7px solid var(--white); }

  .showcase { position: absolute; left: 216px; top: 78px; width: 760px; height: 341px;
    border: 1px solid var(--line); border-top: none; border-radius: 0 0 8px 8px; }
  .hero { position: absolute; left: 8px; top: 9px; width: 751px; height: 274px; border-radius: 6px; overflow: hidden;
    background: linear-gradient(180deg, #5a1d14 0%, #7b3122 22%, #8f4a2e 40%, #b4946a 55%, #c3a679 75%, #b08d61 100%); }
  .hero-dots { position: absolute; left: 10px; top: 10px; display: flex; gap: 7px; }
  .hero-dot { width: 13px; height: 13px; border-radius: 50%; background: rgba(255,255,255,0.45); }
  .hero-dot.is-current { background: var(--white); }
  .hero-title { position: absolute; left: 456px; top: 16px; font-family: "Roboto Condensed", sans-serif; color: var(--white); }
  .hero-title h1 { font-size: 50px; font-weight: 400; line-height: 1; letter-spacing: -1.5px; }
  .hero-title p { font-size: 23px; font-weight: 300; line-height: 24px; margin-top: 4px; letter-spacing: -0.3px; }

  .thumbs { position: absolute; left: 8px; top: 292px; width: 751px; height: 39px; }
  .thumb { position: absolute; top: 0; width: 111px; height: 39px; border-radius: 5px; border: 1px solid #c8d3da;
    background: linear-gradient(90deg, #6b6f5e 0%, #3e4a3a 30%, #334030 100%);
    display: flex; align-items: center; justify-content: flex-start; padding-left: 44px;
    font-family: "Roboto Condensed", sans-serif; font-size: 15px; letter-spacing: -0.3px; color: var(--white); }
  .thumb.is-current { background: linear-gradient(90deg, #c8a882, #a57e5d 50%, #8b6e55); padding-left: 32px; }
  .thumb.is-current::before { content: ""; position: absolute; top: -8px; left: 50%; margin-left: -7px;
    border-left: 7px solid transparent; border-right: 7px solid transparent; border-bottom: 7px solid #c5d9e8; }

  .teaser { position: absolute; top: 418px; height: 167px; border: 1px solid var(--line); border-top: none; border-radius: 0 0 8px 8px; }
  .teaser h2 { position: absolute; left: 16px; top: 10px; font-family: "Roboto Condensed", sans-serif; font-weight: 400;
    font-size: 17.5px; letter-spacing: -0.3px; color: var(--blue); }
  .teaser-photo { position: absolute; left: 17px; top: 40px; width: 73px; height: 121px; border-radius: 5px; border: 2px solid #e4ecf1; }
  .teaser h3 { position: absolute; left: 107px; top: 40px; font-size: 13px; font-weight: 700; color: var(--heading); white-space: nowrap; }
  .teaser p { position: absolute; left: 108px; top: 64px; width: 148px; font-size: 9.6px; line-height: 16.8px; color: var(--text); letter-spacing: 0.15px; }
  .learn-more { position: absolute; top: 596px; width: 84px; height: 18px; border-radius: 9px; background: var(--green);
    font-family: "Roboto Condensed", sans-serif; font-size: 11px; letter-spacing: -0.2px; color: var(--white);
    display: flex; align-items: center; padding-left: 8px; }
  .learn-more svg { position: absolute; right: 0; top: 0; }

  .site-footer { position: absolute; left: 224px; top: 658px; width: 752px; border-top: 1px solid #e3e3e3;
    text-align: center; padding-top: 8px; font-family: "Roboto Condensed", sans-serif; font-size: 11px; color: #666; }
</style>
</head>
<body>
  <div class="brand"><span class="brand-dot"></span><span class="brand-name">47Nova</span></div>

  <nav class="main-nav">
    <div class="nav-item" style="width:56px">HOME</div>
    <div class="nav-item is-active" style="width:70px">COMPANY</div>
    <div class="nav-item" style="width:124px">TECHNICAL SERVICES</div>
    <div class="nav-item" style="width:119px">CREATIVE SERVICES</div>
    <div class="nav-item" style="width:73px">PARTNERS</div>
    <div class="nav-item" style="width:92px">CONTACT US</div>
  </nav>

  <section class="showcase">
    <div class="hero" role="img" aria-label="Photo of a woman in a backbend on a rug in a library beside a laptop">
      <div class="hero-dots">
        <span class="hero-dot"></span><span class="hero-dot is-current"></span><span class="hero-dot"></span>
        <span class="hero-dot"></span><span class="hero-dot"></span><span class="hero-dot"></span>
      </div>
      <div class="hero-title">
        <h1>FLEXIBLE</h1>
        <p>the world moves too fast for<br>rigid solutions</p>
      </div>
    </div>
    <div class="thumbs">
      <div class="thumb" style="left:0" role="img" aria-label="Thumbnail photo: man at a chalkboard">SMART</div>
      <div class="thumb is-current" style="left:128px" role="img" aria-label="Thumbnail photo: woman in a backbend">FLEXIBLE</div>
      <div class="thumb" style="left:255px" role="img" aria-label="Thumbnail photo: man at a chalkboard">SMART</div>
      <div class="thumb" style="left:384px" role="img" aria-label="Thumbnail photo: man at a chalkboard">SMART</div>
      <div class="thumb" style="left:512px" role="img" aria-label="Thumbnail photo: man at a chalkboard">SMART</div>
      <div class="thumb" style="left:639px" role="img" aria-label="Thumbnail photo: man at a chalkboard">SMART</div>
    </div>
  </section>

  <section class="teaser" style="left:216px;width:254px">
    <h2>FOR GRAPHIC DESIGNERS</h2>
    <div class="teaser-photo" style="background:radial-gradient(circle at 50% 40%,#4a5a66 0%,#1b242b 55%,#07090b 100%)" role="img" aria-label="Photo of a man emerging from a cardboard box"></div>
    <h3>Get Creative!</h3>
    <p>47Nova is looking for top creative talent to deliver graphic design solutions for some leading global brands Do you have what it takes?</p>
  </section>
  <a class="learn-more" style="left:386px">LEARN MORE<svg width="18" height="18" viewBox="0 0 18 18"><path d="M0 0h9a9 9 0 0 1 0 18H0z" fill="var(--green-dark)"/><path d="M7 6l3 3-3 3" stroke="#fff" stroke-width="1.2" fill="none"/></svg></a>

  <section class="teaser" style="left:470px;width:259px">
    <h2 style="left:12px">FOR CLIENTS</h2>
    <div class="teaser-photo" style="left:12px;background:linear-gradient(180deg,#e4ddd0 0%,#b9bfc4 50%,#7f8d99 100%)" role="img" aria-label="Photo of colleagues meeting around a table"></div>
    <h3 style="left:100px">The 47Nova Difference</h3>
    <p style="left:100px;width:140px">Smart, Flexible, Thoughtful: find out why leading corporations and government agencies are turning to 47nova to help manage their most demanding IT services challenges.</p>
  </section>
  <a class="learn-more" style="left:645px">LEARN MORE<svg width="18" height="18" viewBox="0 0 18 18"><path d="M0 0h9a9 9 0 0 1 0 18H0z" fill="var(--green-dark)"/><path d="M7 6l3 3-3 3" stroke="#fff" stroke-width="1.2" fill="none"/></svg></a>

  <section class="teaser" style="left:729px;width:247px">
    <h2 style="left:8px">FOR PARTNERS</h2>
    <div class="teaser-photo" style="left:9px;background:linear-gradient(180deg,#dfe4e8 0%,#9aa6b1 45%,#3f4e5e 100%)" role="img" aria-label="Photo of businessmen shaking hands"></div>
    <h3 style="left:99px">Team Up With the Best</h3>
    <p style="left:99px;width:142px">When it comes to technology partnerships, our mission it so make you a success.</p>
  </section>
  <a class="learn-more" style="left:892px">LEARN MORE<svg width="18" height="18" viewBox="0 0 18 18"><path d="M0 0h9a9 9 0 0 1 0 18H0z" fill="var(--green-dark)"/><path d="M7 6l3 3-3 3" stroke="#fff" stroke-width="1.2" fill="none"/></svg></a>

  <footer class="site-footer">Copyright 2010, 47Nova, LLC All rights reserved.</footer>
</body>
</html>
```